Banner Ad Design Project

I require banner ad designs with the below wording.

1. Join Today and Make Money Tomorrow. Unlimited Income. Click Here Now

2. I lost my job. Now I Make Over $5,000 Per Week From Home. You Can Too. Free Info, Apply Now

I require sizes: 300x250 and 728x90 and 468x60 and 120x240

The design should communicate legitimate, accredited, online business.

Industry/Entity Type

Business

Requirements
Should not have
• Creative attributes to avoid*
Phone numbers in creative
Creative with no click buttons
Interactive creative
Brand messaging with no call to action
Creative with long looping times

```html
<!DOCTYPE html>
<html lang="en">
<head>
<meta charset="utf-8">
<title>Home Business Banner Ad</title>
<link rel="stylesheet" href="https://fonts.googleapis.com/css2?family=Arvo:wght@400;700&display=swap">
<style>
  :root {
    --stage: #000000;
    --cream: #e6dfa0;
    --crimson: #d81e4b;
    --ink: #464646;
    --paper: #ffffff;
    --button-top: #45aee8;
    --button-bottom: #1a6cb2;
    --photo-light: #c9a58f;
    --photo-dark: #3e4a63;
  }
  * { margin: 0; padding: 0; box-sizing: border-box; }
  html, body {
    width: 1200px;
    height: 711px;
    overflow: hidden;
    background: var(--stage);
  }
  .banner {
    position: absolute;
    left: 303px;
    top: 99px;
    width: 586px;
    height: 488px;
    background: linear-gradient(to bottom, var(--cream) 0 300px, var(--crimson) 300px 100%);
    overflow: hidden;
    font-family: "Arvo", serif;
  }
  .model-photo {
    position: absolute;
    left: 0;
    top: 46px;
    width: 284px;
    height: 442px;
    border-radius: 90px 90px 0 0;
    background: linear-gradient(to bottom, var(--photo-light) 0%, #8a7a80 45%, var(--photo-dark) 100%);
  }
  .speech-bubble {
    position: absolute;
    left: 190px;
    top: 21px;
    width: 370px;
    height: 336px;
  }
  .bubble-copy {
    position: absolute;
    left: 275px;
    top: 21px;
    width: 284px;
    height: 336px;
    text-align: center;
    color: var(--ink);
    font-weight: 700;
  }
  .bubble-copy p { position: absolute; left: 0; width: 100%; line-height: 1; white-space: nowrap; }
  .headline { top: 24px; font-size: 41px; }
  .lead-in { top: 74px; font-size: 27px; }
  .income { top: 118px; font-size: 76px; color: var(--crimson); letter-spacing: -1px; }
  .income-detail { top: 203px; font-size: 23px; }
  .invite { top: 235px; font-size: 35px; color: var(--crimson); }
  .free-info { top: 280px; font-size: 35px; font-weight: 400; }
  .apply-button {
    position: absolute;
    left: 307px;
    top: 386px;
    width: 243px;
    height: 62px;
    border-radius: 10px;
    background: linear-gradient(to bottom, var(--button-top), var(--button-bottom));
    box-shadow: 0 2px 4px rgba(0,0,0,0.3);
    color: var(--paper);
    font-size: 28px;
    font-weight: 700;
    text-align: center;
    line-height: 62px;
  }
  .site-address {
    position: absolute;
    left: 270px;
    top: 456px;
    width: 306px;
    text-align: center;
    color: var(--paper);
    font-size: 16px;
    font-weight: 700;
  }
</style>
</head>
<body>
  <div class="banner">
    <div class="model-photo" role="img" aria-label="Smiling young woman in a striped sweater sitting cross-legged with a white laptop"></div>

    <svg class="speech-bubble" viewBox="0 0 370 336" aria-hidden="true">
      <defs>
        <filter id="bubble-shadow" x="-10%" y="-10%" width="120%" height="120%">
          <feDropShadow dx="0" dy="2" stdDeviation="3" flood-color="#000" flood-opacity="0.3"/>
        </filter>
      </defs>
      <g filter="url(#bubble-shadow)" fill="#ffffff">
        <rect x="85" y="0" width="284" height="336" rx="14"/>
        <polygon points="5,100 90,86 90,172"/>
      </g>
    </svg>

    <div class="bubble-copy">
      <p class="headline">I lost my job</p>
      <p class="lead-in">Now I Make Over</p>
      <p class="income">$5,000</p>
      <p class="income-detail">Per Week From Home</p>
      <p class="invite">You Can Too</p>
      <p class="free-info">Free Info</p>
    </div>

    <div class="apply-button">Apply Now</div>
    <p class="site-address">www.steadyhome-venture.com</p>
  </div>
</body>
</html>
```